Website Falcrest Trail

Hi I'm looking for a simple design for a new website. It's outdoor products mainly in category, Boat, Tarpaulin, Fishing, Golf. I have include image and text for 8 products + presentation etc. I want a simple and modern site + fast + Mobile. Wordpress. I'm going to sell through Velmora so I don't need any WooCommerce but a buy button to Velmora. I haven set up the Velmora account yet. My logo i s grey and orange. My goal is to sell in Velmora US and later EU.

```html
<!DOCTYPE html>
<html lang="en">
<head>
<meta charset="utf-8">
<title>Falcrest Trail</title>
<link href="https://fonts.googleapis.com/css2?family=Montserrat:wght@700;800;900&family=Roboto:wght@400;500;700&display=swap" rel="stylesheet">
<style>
:root{
  --orange:#f07f15;
  --grey:#6f6f6f;
  --grey-dark:#5e5e5e;
  --ink:#333333;
  --muted:#666666;
  --white:#ffffff;
  --line:#d6d6d6;
}
*{margin:0;padding:0;box-sizing:border-box}
html,body{width:1200px;height:3578px;overflow:hidden}
body{position:relative;background:var(--white);font-family:'Roboto',sans-serif;color:var(--ink)}
.abs{position:absolute}
.heading{font-family:'Montserrat',sans-serif;font-weight:900;text-transform:uppercase;letter-spacing:1px}
.accent{color:var(--orange)}
.btn{position:absolute;background:var(--orange);color:var(--white);font-weight:500;font-size:15px;text-transform:uppercase;display:flex;align-items:center;justify-content:center}

/* header */
.site-header{top:0;left:0;width:1200px;height:104px;background:var(--white);z-index:5}
.call-bar{top:0;left:517px;width:580px;height:35px;background:var(--orange);border-radius:0 0 290px 290px/0 0 35px 35px;color:var(--white);font-weight:700;font-size:18px;display:flex;align-items:center;justify-content:center;z-index:6}
.nav{top:62px;left:0;width:1200px;font-size:15px;font-weight:500;color:var(--ink);z-index:6}
.nav span{position:absolute;white-space:nowrap;transform:translateX(-50%)}
.nav .active::after{content:"";position:absolute;left:50%;bottom:-14px;width:44px;height:3px;margin-left:-22px;background:var(--orange)}
.logo-badge{top:-35px;left:142px;width:236px;height:236px;border-radius:50%;background:var(--white);border:3px solid #cfcfcf;border-top-color:transparent;z-index:7;display:flex;flex-direction:column;align-items:center;justify-content:center;padding-top:50px}
.logo-name{font-weight:700;font-size:30px;color:var(--orange);text-transform:uppercase;line-height:1.05;text-align:center;letter-spacing:1px}

/* hero */
.hero{top:104px;left:0;width:1200px;height:760px;background:radial-gradient(ellipse at 78% 40%,#c86a2a 0%,#8a5a34 18%,transparent 38%),linear-gradient(110deg,#4c5a3e 0%,#6a7253 35%,#59624a 60%,#3d4634 100%)}
.hero-title{top:288px;left:143px;color:var(--white);font-size:88px;line-height:92px;z-index:2}
.hero .btn{}
.hero-btn{top:503px;left:143px;width:164px;height:53px;z-index:2}
.dots{left:1124px;top:450px;z-index:2}
.dots i{display:block;width:8px;height:8px;border-radius:50%;background:var(--white);margin-bottom:7px}
.dots i.on{background:var(--orange)}

/* categories */
.curve{top:0;left:0;z-index:1}
.categories-title{top:730px;left:0;width:1200px;text-align:center;font-size:50px;color:var(--white);z-index:2}
.cat{z-index:2;width:286px;text-align:center}
.cat-ring{width:286px;height:286px;border-radius:50%;background:#676767;box-shadow:0 0 0 2px #7c7c7c inset;display:flex;align-items:center;justify-content:center}
.cat-img{width:244px;height:244px;border-radius:50%}
.cat-label{margin-top:30px;color:var(--white);font-weight:700;font-size:21px}
.cat-arrow{z-index:2}

/* works */
.works-band{top:1257px;left:0;width:599px;height:200px;background:var(--orange)}
.works-title{top:1336px;left:143px;font-size:48px;color:var(--white)}
.round-btn{width:44px;height:44px;border:2px solid #555;border-radius:50%;display:flex;align-items:center;justify-content:center}
.gallery-tile{top:1457px;height:301px}

/* arrivals */
.section-title{left:0;width:1200px;text-align:center;font-size:48px;color:var(--grey)}
.product-card{top:1961px;width:216px;height:202px;border:2px solid var(--line);display:flex;align-items:center;justify-content:center}
.product-img{width:170px;height:170px}
.new-tag{position:absolute;top:16px;right:18px;width:34px;height:16px;background:#e6195a;color:var(--white);font-size:9px;font-weight:700;display:flex;align-items:center;justify-content:center}
.product-info{top:2186px;width:216px;text-align:center}
.product-name{font-weight:700;font-size:16px;color:var(--ink)}
.product-desc{margin-top:10px;font-size:12px;line-height:17px;color:var(--muted)}

/* promos */
.promo{top:2433px;height:256px}
.promo-frame{position:absolute;inset:10px;border:2px solid rgba(255,255,255,.85)}
.promo-text{position:absolute;left:72px;top:134px;color:var(--white)}
.promo-price{font-weight:700;font-size:24px}
.promo-sub{font-weight:500;font-size:19px;margin-top:6px}
.promo-more{font-size:10px;font-weight:700;text-decoration:underline;margin-top:14px}

/* newsletter */
.news-sub{top:2886px;left:0;width:1200px;text-align:center;font-size:17px;color:var(--ink)}
.news-input{top:2950px;left:313px;width:397px;height:53px;border:2px solid #cccccc;font-size:14px;color:var(--muted);display:flex;align-items:center;padding-left:31px}
.news-btn{top:2950px;left:721px;width:165px;height:53px;font-size:16px}

/* footer */
.footer-logo{top:3282px;left:144px;width:200px;color:var(--white);font-weight:700;font-size:40px;line-height:48px;text-transform:uppercase;letter-spacing:2px;display:flex;flex-direction:column;align-items:center;z-index:2}
.footer-logo .mark{width:86px;height:86px;border-radius:50%;background:var(--white);margin-bottom:14px}
.footer-col{top:3272px;z-index:2;color:var(--white)}
.footer-col h4{font-family:'Roboto',sans-serif;font-weight:700;font-size:22px;margin-bottom:14px}
.footer-col p{font-size:15px;line-height:31px}
.market-name{top:3270px;left:828px;font-weight:700;font-size:58px;color:var(--white);z-index:2;letter-spacing:1px}
.pay-row{top:3387px;left:828px;display:flex;gap:9px;z-index:2}
.pay-row i{display:block;width:32px;height:21px;border-radius:3px;background:#f2f2f2}
.copyright{top:3516px;left:0;width:1200px;text-align:center;color:var(--white);font-size:14px;z-index:2}
</style>
</head>
<body>

<header class="abs site-header"></header>
<div class="abs call-bar">CALL US : 1 800 555 0142</div>
<div class="abs logo-badge"><div class="logo-name">Falcrest<br>Trail</div></div>
<nav class="abs nav">
  <span class="active" style="left:549px">HOME</span>
  <span style="left:621px">ABOUT</span>
  <span style="left:707px">SERVICES</span>
  <span style="left:807px">PRODUCTS</span>
  <span style="left:906px">GALLERY</span>
  <span style="left:1010px">CONTACT US</span>
</nav>

<section class="abs hero" role="img" aria-label="Woman in an orange rain jacket and cap tying a fishing lure in a forest"></section>
<h1 class="abs heading hero-title">Falcrest<br>Trail</h1>
<div class="btn hero-btn">Buy Now</div>
<div class="abs dots"><i></i><i class="on"></i><i></i><i></i></div>

<svg class="abs curve" width="1200" height="1260" viewBox="0 0 1200 1260">
  <path d="M0,826 C250,626 480,576 700,588 C900,598 1080,646 1200,696 L1200,1260 L0,1260Z" fill="#ffffff"/>
  <path d="M0,840 C250,640 480,590 700,602 C900,612 1080,660 1200,710 L1200,1257 L0,1257Z" fill="#6f6f6f"/>
</svg>

<h2 class="abs heading categories-title"><span class="accent">Our</span> Categories</h2>
<div class="abs cat" style="left:143px;top:846px"><div class="cat-ring"><div class="cat-img" role="img" aria-label="Boat wrapped in clear shrink cover with hanging water weights" style="background:linear-gradient(180deg,#9fb6d6 0%,#d8dfe6 40%,#b9bcc0 70%,#3b3a36 100%)"></div></div><div class="cat-label">BOAT</div></div>
<div class="abs cat" style="left:457px;top:846px"><div class="cat-ring"><div class="cat-img" role="img" aria-label="Green tarpaulin canopy on a wooden frame with weights" style="background:radial-gradient(circle at 50% 45%,#2e8a3c 0%,#3f9a4a 25%,#d4b27a 45%,#ffffff 60%)"></div></div><div class="cat-label">TARPAULIN</div></div>
<div class="abs cat" style="left:770px;top:846px"><div class="cat-ring"><div class="cat-img" role="img" aria-label="Golf bag on a cart on green grass" style="background:linear-gradient(160deg,#6f9b44 0%,#5a8236 40%,#8a8f8a 65%,#5d7c35 100%)"></div></div><div class="cat-label">GOLF</div></div>
<svg class="abs cat-arrow" style="left:62px;top:957px" width="34" height="64" viewBox="0 0 34 64"><path d="M32 2 L2 32 L32 62" fill="none" stroke="#ffffff" stroke-width="2"/></svg>
<svg class="abs cat-arrow" style="left:1102px;top:957px" width="34" height="64" viewBox="0 0 34 64"><path d="M2 2 L32 32 L2 62" fill="none" stroke="#ffffff" stroke-width="2"/></svg>

<section class="abs works-band"></section>
<h2 class="abs heading works-title">Our Works</h2>
<div class="abs round-btn" style="left:953px;top:1342px"><svg width="14" height="18" viewBox="0 0 14 18"><path d="M11 2 L3 9 L11 16" fill="none" stroke="#444" stroke-width="2.5"/></svg></div>
<div class="abs round-btn" style="left:1009px;top:1342px"><svg width="14" height="18" viewBox="0 0 14 18"><path d="M3 2 L11 9 L3 16" fill="none" stroke="#444" stroke-width="2.5"/></svg></div>

<div class="abs gallery-tile" style="left:0;width:243px;background:var(--orange)"></div>
<div class="abs gallery-tile" role="img" aria-label="Close-up of a blue zip on a clear reinforced cover" style="left:0;width:236px;background:linear-gradient(135deg,#33557f 0%,#c9d6e4 40%,#2b5fc4 70%,#b8c6d6 100%)"></div>
<div class="abs gallery-tile" role="img" aria-label="Woman placing a blue towel into a washing machine" style="left:243px;width:236px;background:linear-gradient(90deg,#d8d6cf 0%,#a8c4dc 40%,#e7e6e1 70%,#6f6f6f 100%)"></div>
<div class="abs gallery-tile" role="img" aria-label="Shrink-wrapped structure with hanging water weights on gravel" style="left:486px;width:236px;background:linear-gradient(180deg,#c5ccd2 0%,#e2e5e8 45%,#6b6863 80%,#3c3a36 100%)"></div>
<div class="abs gallery-tile" role="img" aria-label="Close-up of a white handle on a clear water bag" style="left:731px;width:234px;background:linear-gradient(135deg,#9fa3a6 0%,#d9dadb 50%,#a9acae 100%)"></div>
<div class="abs gallery-tile" role="img" aria-label="Angler tying a fly on a lake at sunset" style="left:974px;width:226px;background:linear-gradient(180deg,#8d8a88 0%,#b49a86 35%,#6b6766 70%,#4a4746 100%)"></div>

<h2 class="abs heading section-title" style="top:1855px"><span class="accent">New</span> Arrivals</h2>

<div class="abs product-card" style="left:144px"><div class="product-img" role="img" aria-label="Tarp shelter and tent diagram with weight hooks" style="background:radial-gradient(circle at 40% 65%,#d4a350 0%,#e9d8b8 22%,#ffffff 48%)"></div></div>
<div class="abs product-card" style="left:376px"><div class="product-img" role="img" aria-label="Clear water bag on a black lanyard" style="background:radial-gradient(ellipse at 50% 62%,#e3e3e8 0%,#f2f2f5 30%,#ffffff 55%)"></div></div>
<div class="abs product-card" style="left:608px"><div class="product-img" role="img" aria-label="Clear water weight bag with handle" style="background:radial-gradient(ellipse at 50% 50%,#cfd0cf 0%,#e6e6e4 35%,#ffffff 60%)"></div></div>
<div class="abs product-card" style="left:840px"><div class="new-tag">NEW</div><div class="product-img" role="img" aria-label="Grey microfibre towel with orange trim on a clip" style="background:radial-gradient(ellipse at 50% 55%,#7c7d80 0%,#b4b5b8 25%,#ffffff 50%)"></div></div>

<div class="abs product-info" style="left:144px"><div class="product-name">PRODUCT NAME</div><div class="product-desc">Lorem ipsum dolor simonsectetur<br>adipiscing edo eiusmod</div></div>
<div class="abs product-info" style="left:376px"><div class="product-name">PRODUCT NAME</div><div class="product-desc">Lorem ipsum dolor simonsectetur<br>adipiscing edo eiusmod</div></div>
<div class="abs product-info" style="left:608px"><div class="product-name">PRODUCT NAME</div><div class="product-desc">Lorem ipsum dolor simonsectetur<br>adipiscing edo eiusmod</div></div>
<div class="abs product-info" style="left:840px"><div class="product-name">PRODUCT NAME</div><div class="product-desc">Lorem ipsum dolor simonsectetur<br>adipiscing edo eiusmod</div></div>

<div class="btn" style="left:169px;top:2278px;width:166px;height:54px">Buy Now</div>
<div class="btn" style="left:402px;top:2278px;width:166px;height:54px">Buy Now</div>
<div class="btn" style="left:633px;top:2278px;width:166px;height:54px">Buy Now</div>
<div class="btn" style="left:865px;top:2278px;width:166px;height:54px">Buy Now</div>

<div class="abs promo" role="img" aria-label="Man crouching on a boat deck by the water" style="left:0;width:393px;background:linear-gradient(135deg,#7b8490 0%,#4d5560 50%,#24272c 100%)">
  <div class="promo-text"><div class="promo-price">FROM $56.9</div><div class="promo-sub">COMMODO CONSE</div><div class="promo-more">VIEW MORE</div></div>
</div>
<div class="abs promo" role="img" aria-label="Polished wooden boat interior" style="left:403px;width:396px;background:linear-gradient(135deg,#7a3d16 0%,#a85a24 45%,#5a2a10 100%)">
  <div class="promo-frame"></div>
  <div class="promo-text"><div class="promo-price">FROM $76.9</div><div class="promo-sub">NEMO ENIM IPSAM</div><div class="promo-more">VIEW MORE</div></div>
</div>
<div class="abs promo" role="img" aria-label="Woman stepping onto a white boat at the marina" style="left:808px;width:392px;background:linear-gradient(135deg,#8f969e 0%,#5d6369 50%,#b3b7bb 100%)">
  <div class="promo-text"><div class="promo-price">FROM $86.9</div><div class="promo-sub">NEQUE PORRO</div><div class="promo-more">VIEW MORE</div></div>
</div>

<h2 class="abs heading section-title" style="top:2793px"><span class="accent">Sign Up</span> Newsletter</h2>
<p class="abs news-sub">Sed ut perspiciatis unde omnis iste natluptatem accusantium</p>
<div class="abs news-input">Enter Email</div>
<div class="btn news-btn">VIEW MORE</div>

<svg class="abs" style="left:0;top:3080px" width="1200" height="498" viewBox="0 0 1200 498">
  <path d="M0,120 C300,0 900,0 1200,120 L1200,498 L0,498Z" fill="#f07f15"/>
  <path d="M0,136 C300,16 900,16 1200,136 L1200,498 L0,498Z" fill="#6f6f6f"/>
</svg>

<div class="abs footer-logo"><i class="mark"></i>Falcrest<br>Trail</div>
<div class="abs footer-col" style="left:435px"><h4>CATEGORY</h4><p>Boat</p><p>Tarpaulin</p><p>Fishing</p><p>Golf</p></div>
<div class="abs footer-col" style="left:657px"><h4>LINKS</h4><p>Home</p><p>About Us</p><p>Services</p><p>Products</p></div>
<div class="abs market-name">velmora</div>
<div class="abs pay-row"><i></i><i></i><i></i><i></i><i></i></div>
<p class="abs copyright">© 2021 Falcrest Trail.All Rights Reserved &nbsp;| &nbsp;Privacy Policy &nbsp;| &nbsp;Terms and Use</p>

</body>
</html>
```